Meadowtail Pet Business Card

We need a business card designed with two sides to it. I would like the front of the card to be mostly graphic and the back of the card to have the bullet points of our pet food.

I don't have a telephone number for the business yet so just leave a space for a toll free number. (800) xxx-xxxx.

Thanks,

Tobias

Combination Diet
Chicken Diet
Beef Diet
Lamb Diet

Website:  www.meadowtailpet-example.net

email:  rwelby@meadowtailpet-example.net

Direct - 347-xxx-xxxx
Toll Free - xxx-xxx-xxxx

www.meadowtailpet-example.net

Ravi Welby (Example)
Customer Experience Officer

rwelby@meadowtailpet-example.net
Direct - (347) xxx-xxxx

Sales Inquiries - (800) xxx-xxxx

All,

Please include the following items on the back of the business card.

Combination Diet
Chicken Diet
Beef Diet
Lamb Diet
 

Thanks,

Tobias

All, I will also want a QR code on the front or back of the card that can be scanned by a smart phone with our individual contact information.  Thanks, Tobias

Industry/Entity Type

Pet

```html
<!DOCTYPE html>
<html lang="en">
<head>
<meta charset="utf-8">
<title>Meadowtail Pet Business Card</title>
<link rel="stylesheet" href="https://fonts.googleapis.com/css2?family=Open+Sans:wght@400;600;700&display=swap">
<style>
  :root {
    --page: #ffffff;
    --card: #2a150c;
    --rust: #c2492a;
    --orange: #e8822a;
    --amber: #ec9a35;
    --gold: #f5c51c;
    --white: #ffffff;
    --label: #333333;
  }
  * { margin: 0; padding: 0; box-sizing: border-box; }
  html, body {
    width: 1200px; height: 1024px; overflow: hidden;
    background: var(--page);
    font-family: "Open Sans", Arial, sans-serif;
  }
  .canvas { position: relative; width: 1200px; height: 1024px; }
  .card {
    position: absolute; top: 202px; width: 374px; height: 617px;
    background: var(--card);
    text-align: center;
  }
  .card--front { left: 192px; }
  .card--back { left: 629px; }

  .brand {
    position: absolute; top: 86px; left: 0; right: 0;
    font-size: 30px; line-height: 44px; font-weight: 700; color: var(--orange);
  }

  .person { position: absolute; left: 0; right: 0; top: 198px; }
  .person-name { font-size: 20px; line-height: 26px; font-weight: 700; color: var(--white); text-transform: uppercase; }
  .person-title { font-size: 20px; line-height: 30px; color: var(--orange); margin-top: 2px; }

  .contact { position: absolute; left: 0; right: 0; font-size: 17px; line-height: 41px; white-space: nowrap; }
  .contact--online { top: 316px; }
  .contact--phone { top: 440px; line-height: 40px; }
  .contact-label { color: var(--rust); font-weight: 700; text-transform: uppercase; }
  .contact-value { color: var(--orange); }

  .diet-list { list-style: none; }
  .diet {
    position: absolute; left: 0; right: 0;
    font-size: 26px; line-height: 36px;
    text-transform: uppercase; white-space: nowrap;
  }
  .diet--combination { top: 80px; }
  .diet--chicken { top: 215px; }
  .diet--beef { top: 349px; }
  .diet--lamb { top: 479px; }
  .diet-name { font-weight: 700; }
  .diet-word { font-weight: 400; }
  .diet--combination { color: var(--rust); }
  .diet--chicken .diet-name { color: var(--rust); }
  .diet--chicken .diet-word { color: var(--orange); }
  .diet--beef { color: var(--amber); }
  .diet--lamb .diet-name { color: var(--gold); }
  .diet--lamb .diet-word { color: var(--amber); }

  .side-label {
    position: absolute; top: 864px; width: 374px;
    font-size: 18px; line-height: 24px; color: var(--label); text-align: center; text-transform: uppercase;
  }
  .side-label--front { left: 192px; }
  .side-label--back { left: 629px; }
</style>
</head>
<body>
<main class="canvas">
  <section class="card card--front" aria-label="Card front">
    <p class="brand">Meadowtail Pet</p>
    <div class="person">
      <p class="person-name">Ravi Welby</p>
      <p class="person-title">Customer experience officer</p>
    </div>
    <div class="contact contact--online">
      <p><span class="contact-label">Email:</span><span class="contact-value">rwelby@meadowtailpet-example.net</span></p>
      <p><span class="contact-label">Website:</span><span class="contact-value">www.meadowtailpet-example.net</span></p>
    </div>
    <div class="contact contact--phone">
      <p><span class="contact-label">Toll free:</span><span class="contact-value">xxx-xxx-xxxx</span></p>
      <p><span class="contact-label">Sales inquiries:</span><span class="contact-value">(800)xxx-xxxx</span></p>
      <p><span class="contact-label">Direct:</span><span class="contact-value">(347)xxx-xxxx</span></p>
    </div>
  </section>

  <section class="card card--back" aria-label="Card back">
    <ul class="diet-list">
      <li class="diet diet--combination"><span class="diet-name">Combination</span>&nbsp; <span class="diet-word">Diet</span></li>
      <li class="diet diet--chicken"><span class="diet-name">Chicken</span> <span class="diet-word">Diet</span></li>
      <li class="diet diet--beef"><span class="diet-name">Beef</span> <span class="diet-word">Diet</span></li>
      <li class="diet diet--lamb"><span class="diet-name">Lamb</span> <span class="diet-word">Diet</span></li>
    </ul>
  </section>

  <p class="side-label side-label--front">Front</p>
  <p class="side-label side-label--back">Back</p>
</main>
</body>
</html>
```